Therapy Dog Organization Website

Looking for a website that is user friendly, welcoming, dog themed and has the following pages and links:
*Click here to join - links to a jot form
*Click here to donate - links to our paypal page
*Request a visit - links to a jot form
*Facebook Follow Link
*Instagram Follow Link
*Our team - images uploaded to showcase our dogs
*Donors and Referrals Page - Where I can update as donations and referrals come in.
*Online store. Currently this is in Jot Form but I would like a store front. I would not want this to be a link but rather a hidden page, something like www.hollowbirch.org/teamstore.

Please visit www.hollowbirch.org to see what we have right now designed simply in Canva. Dog photos can be provided to use in images.

Note: I have funds from a grant that I have to spend to add gratuity to the project winner.

```html
<!DOCTYPE html>
<html lang="en">
<head>
<meta charset="utf-8">
<title>HollowBirch Therapy Dogs</title>
<link rel="stylesheet" href="https://fonts.googleapis.com/css2?family=Anton&family=Poppins:wght@400;500;600;700&display=swap">
<style>
:root{
  --sky:#67c4ee;
  --purple:#2d0c57;
  --yellow:#f9b73b;
  --ink:#1b1b1b;
  --grey:#f3f3f3;
  --white:#ffffff;
  --line:#6b6b8a;
  --placeholder:#e6e6ea;
}
*{box-sizing:border-box;margin:0;padding:0}
html,body{width:1200px;height:5008px;overflow:hidden}
body{font-family:"Poppins",sans-serif;color:var(--ink);background:var(--white);position:relative}
.abs{position:absolute}
.display{font-family:"Anton",sans-serif;font-weight:400;letter-spacing:.5px;text-transform:uppercase}
.btn{position:absolute;display:flex;align-items:center;justify-content:center;border-radius:22px;font-size:14px;font-weight:600;height:40px}
.btn-yellow{background:var(--yellow);color:var(--purple)}
.btn-purple{background:var(--purple);color:var(--white)}
p{font-size:14.5px;line-height:1.78}

/* header + hero */
.top{position:absolute;left:0;top:0;width:1200px;height:750px;background:var(--sky)}
.brand{position:absolute;display:flex;align-items:center;gap:10px;color:var(--purple);font-weight:600}
.brand .dot{width:30px;height:30px;border-radius:50%;background:var(--purple)}
.brand .name{font-size:26px;line-height:1}
.brand .sub{font-size:15px;letter-spacing:2px;line-height:1.2}
.nav{position:absolute;left:352px;top:46px;display:flex;gap:22px;font-size:13.5px;color:var(--purple)}
.hero-photo{position:absolute;border-radius:42px;background:linear-gradient(135deg,#6f5a43,#a48b68 40%,#3b3a3d 75%,#1f2d3a)}
.hero-title{left:170px;top:455px;font-size:46px;color:var(--white)}
.hero-text{left:170px;top:528px;width:520px;color:var(--white);font-size:16px;line-height:1.9}

/* story */
.story-photo{left:0;top:868px;width:617px;height:587px;border-radius:0 40px 40px 0;background:linear-gradient(120deg,#2a2f55,#6f4c3b 45%,#b34a4a 70%,#2b2e3d)}
.badge-placeholder{border-radius:50%;background:var(--placeholder)}
.h2{font-size:44px;color:var(--ink)}

/* mission */
.mission-bg{left:0;top:1560px;width:592px;height:702px;background:var(--purple)}
.mission-photo{left:592px;top:1560px;width:608px;height:702px;background:linear-gradient(160deg,#4a4746,#7a4a32 50%,#3a2b25)}
.grey-band{left:0;top:2262px;width:1200px;height:1113px;background:var(--grey)}
.purpose-card{background:var(--sky)}
.purpose-photo{left:174px;top:2160px;width:407px;height:480px;border-radius:22px;background:linear-gradient(135deg,#7c7a78,#2c2a2a 50%,#c9b8a4)}

/* team */
.team-card{position:absolute;top:2888px;width:237px;height:297px;background:var(--white);border-radius:8px;box-shadow:0 2px 6px rgba(0,0,0,.08)}
.team-card .pic{position:absolute;left:8px;top:8px;right:8px;height:235px;border-radius:4px}
.team-card .label{position:absolute;left:0;right:0;bottom:12px;text-align:center;font-size:20px}
.arrow{position:absolute;top:3230px;width:44px;height:44px;border-radius:50%;border:2px solid var(--purple);display:flex;align-items:center;justify-content:center}

/* donors */
.tag{position:absolute;top:3705px;width:190px;height:45px;display:flex;align-items:center;justify-content:center;font-size:14px;font-weight:600}
.tag::after{content:"";position:absolute;bottom:-10px;left:50%;margin-left:-10px;border-left:10px solid transparent;border-right:10px solid transparent;border-top:10px solid currentColor}
.box{position:absolute;top:3770px;width:314px;height:400px;border-radius:22px;text-align:center;padding:50px 16px 0}
.box h3{font-size:16px;font-weight:600;margin-bottom:16px}
.box p{font-size:13.5px;line-height:1.85}
.donor-list{list-style:none;text-align:left;padding-left:60px}
.donor-list li{font-size:16px;font-weight:600;color:var(--purple);line-height:38.5px;display:flex;align-items:center;gap:14px}
.donor-list li::before{content:"";width:12px;height:12px;border-radius:50%;background:var(--purple)}
.mark{width:14px;height:14px;border-radius:50%;margin:16px auto}

/* footer */
.footer{left:0;top:4595px;width:1200px;height:413px;background:var(--sky)}
.footer-tab{left:46px;top:4550px;width:1109px;height:120px;background:var(--sky);border-radius:46px 46px 0 0}
.social{position:absolute;top:4650px;width:40px;height:40px;border-radius:50%;border:2px solid var(--purple)}
.flinks{left:515px;top:4780px;width:572px;display:flex;justify-content:space-between;font-size:14px;color:var(--purple);text-decoration:underline}
</style>
</head>
<body>

<!-- header & hero -->
<div class="top"></div>
<div class="brand" style="left:85px;top:18px">
  <span class="dot"></span>
  <div><div class="name">HollowBirch</div><div class="sub">Therapy Dogs</div></div>
</div>
<nav class="nav"><span>About</span><span>Our Team</span><span>Request a Visit</span><span>Donors &amp; Referrals</span><span>Contact</span></nav>
<div class="btn btn-purple" style="left:876px;top:37px;width:88px">Donate</div>
<div class="btn btn-yellow" style="left:974px;top:37px;width:142px">Join Our Team</div>

<div class="hero-photo" role="img" aria-label="Three therapy dogs in bandanas and vests sitting together in an office" style="left:85px;top:150px;width:1030px;height:550px"></div>
<div class="hero-photo" role="img" aria-label="Therapy dogs hero photograph" style="left:128px;top:108px;width:944px;height:642px;border-radius:0"></div>
<h1 class="abs display hero-title">One Paw at a Time.</h1>
<p class="abs hero-text">A Michigan Nonprofit dedicated to providing Therapy Dogs to the community to spread joy, hope and healing.</p>
<div class="btn btn-yellow" style="left:170px;top:618px;width:254px">Request a Therapy Visit</div>
<div class="btn btn-purple" style="left:437px;top:618px;width:182px">Join Our Team</div>

<!-- story -->
<div class="abs story-photo" role="img" aria-label="A child hugging a therapy dog wearing a vest on a carpet"></div>
<div class="abs badge-placeholder" role="img" aria-label="Certification badge placeholder" style="left:475px;top:1190px;width:175px;height:175px"></div>
<h2 class="abs display h2" style="left:715px;top:955px">Our Story</h2>
<p class="abs" style="left:715px;top:1033px;width:380px">Every wag tells a story – and ours began with a simple belief: <b>the love of a dog can change lives.</b></p>
<p class="abs" style="left:715px;top:1096px;width:380px">What started with a few volunteers and their dogs has grown into a community dedicated to bringing comfort and joy wherever it's needed most. From hospitals to schools and senior centers, our therapy dog teams share moments of connection, calm, and healing – <b>one visit at a time.</b></p>
<div class="btn btn-yellow" style="left:715px;top:1307px;width:182px">See Our Impact</div>

<!-- mission -->
<div class="abs mission-bg"></div>
<div class="abs mission-photo" role="img" aria-label="A Doberman therapy dog lying beside a plush toy dog, both in bandanas"></div>
<div class="abs grey-band"></div>
<h2 class="abs display h2" style="left:112px;top:1685px;color:var(--white)">Our Mission</h2>
<p class="abs" style="left:112px;top:1762px;width:470px;color:var(--white);font-weight:600">To certify, and deploy therapy dog teams that promote emotional well-being, reduce stress, and foster empathy.</p>
<p class="abs" style="left:112px;top:1825px;width:480px;color:var(--white)">We are dedicated to improving quality of life by bringing the unconditional love and calming presence of therapy dogs to those in need, while upholding the highest standards of animal welfare, professionalism, and community service.</p>
<div class="btn btn-yellow" style="left:112px;top:1965px;width:184px">Join Our Mission</div>

<div class="abs purpose-card" style="left:130px;top:2100px;width:940px;height:585px;border-radius:42px"></div>
<div class="abs purpose-card" style="left:84px;top:2148px;width:1031px;height:492px"></div>
<div class="abs purpose-photo" role="img" aria-label="Collage of a shepherd therapy dog visiting people"></div>
<div class="abs" style="left:275px;top:2348px;width:110px;height:110px;border-radius:50%;background:var(--white);display:flex;align-items:center;justify-content:center;font-size:13px;font-weight:600;color:var(--purple)">HollowBirch</div>
<h2 class="abs display h2" style="left:638px;top:2225px">Our Purpose</h2>
<p class="abs" style="left:638px;top:2298px;width:425px;font-size:14px">Our purpose is to share the comfort, joy, and healing power of the human animal bond. We connect trained therapy dog teams with people in need of emotional support, companionship, and encouragement in hospitals, schools, senior communities, and beyond.</p>
<p class="abs" style="left:638px;top:2447px;width:425px;font-size:14px;font-weight:600">Through every visit, we aim to lift spirits, ease stress, and remind people that kindness and connection can come on four paws and a wagging tail.</p>
<div class="btn btn-yellow" style="left:638px;top:2542px;width:184px">Join Our Team</div>

<!-- team -->
<h2 class="abs display h2" style="left:0;width:1200px;text-align:center;top:2800px">Our Team</h2>
<div class="team-card" style="left:-45px"><div class="pic" role="img" aria-label="Sky, a fluffy husky mix in a pink bandana" style="background:linear-gradient(135deg,#8a6a52,#e9e3dc)"></div><div class="label display">Meet Sky</div></div>
<div class="team-card" style="left:205px"><div class="pic" role="img" aria-label="Luna, a fluffy husky mix in a pink bandana" style="background:linear-gradient(135deg,#7a5d48,#e3d4c0)"></div><div class="label display">Meet Luna</div></div>
<div class="team-card" style="left:459px"><div class="pic" role="img" aria-label="Nova, a merle dog in a pink bandana" style="background:linear-gradient(135deg,#6e5a4a,#9fa3a8)"></div><div class="label display">Meet Nova</div></div>
<div class="team-card" style="left:710px"><div class="pic" role="img" aria-label="Stoick, a golden retriever" style="background:linear-gradient(135deg,#b6742e,#e0a75c)"></div><div class="label display">Meet Stoick</div></div>
<div class="team-card" style="left:961px"><div class="pic" role="img" aria-label="Sven, a golden retriever lying on grass" style="background:linear-gradient(160deg,#c9d6e4,#d9a45b 45%,#7c8a44)"></div><div class="label display">Meet Sven</div></div>
<div class="abs" style="left:245px;top:3252px;width:290px;height:1px;background:var(--line)"></div>
<div class="abs" style="left:665px;top:3252px;width:290px;height:1px;background:var(--line)"></div>
<div class="arrow" style="left:549px"><svg width="18" height="18" viewBox="0 0 18 18"><path d="M15 9H3M8 4L3 9l5 5" fill="none" stroke="#2d0c57" stroke-width="2"/></svg></div>
<div class="arrow" style="left:606px"><svg width="18" height="18" viewBox="0 0 18 18"><path d="M3 9h12M10 4l5 5-5 5" fill="none" stroke="#2d0c57" stroke-width="2"/></svg></div>

<!-- donors -->
<h2 class="abs display h2" style="left:0;width:1200px;text-align:center;top:3480px">Donors &amp; Referrals</h2>
<p class="abs" style="left:300px;width:600px;text-align:center;top:3560px;font-size:14px"><b>Our donors and referral partners are the heart of our organization.</b> Because of their generosity, we are able to keep costs low for our therapy dog teams while never compromising the integrity, training, and care of our handlers and dogs.</p>

<div class="tag" style="left:174px;background:var(--yellow);color:var(--yellow)"><span style="color:var(--purple)">Individual Donors</span></div>
<div class="tag" style="left:505px;background:var(--purple);color:var(--purple)"><span style="color:var(--white)">Corporate Donors</span></div>
<div class="tag" style="left:836px;background:var(--sky);color:var(--sky)"><span style="color:var(--purple)">Referrals</span></div>

<div class="box" style="left:112px;background:var(--yellow);padding-top:44px">
  <ul class="donor-list">
    <li>Martin Hale</li><li>Owen Baskerville</li><li>Gerald Winslow</li><li>Ruth Callahan</li><li>Dana Whitcomb</li><li>Peter Anders</li><li>Lloyd Farrow</li>
  </ul>
</div>
<div class="box" style="left:443px;background:var(--purple);color:var(--white)">
  <h3>Linewise</h3>
  <p>Cloud Phone Systems Build for Reliable Business Communications</p>
  <div class="mark" style="background:var(--white)"></div>
  <h3 style="margin-bottom:10px">Cedar Ridge Post 12<br>Veterans Hall</h3>
  <p>Serving Veterans from the local community since 1930. To all who have served America: <b>THANK YOU!</b></p>
</div>
<div class="box" style="left:774px;background:var(--sky);color:var(--purple)">
  <h3>Steadfast Canine Training</h3>
  <p>Northern Michigan Dog Training Facility. Bridging the communication gap between dogs &amp; owners.</p>
  <div class="mark" style="background:var(--purple)"></div>
</div>

<h2 class="abs display" style="left:0;width:1200px;text-align:center;top:4230px;font-size:46px;color:var(--purple);text-transform:none">Thank you</h2>
<p class="abs" style="left:250px;width:700px;text-align:center;top:4308px;font-size:21px;line-height:1.7;font-weight:500">for believing in our mission and helping us spread healing one paw at a time.</p>
<div class="btn btn-yellow" style="left:474px;top:4406px;width:252px">Donate Today</div>

<!-- footer -->
<div class="abs footer-tab"></div>
<div class="abs footer"></div>
<div class="brand" style="left:112px;top:4645px">
  <span class="dot" style="width:38px;height:38px"></span>
  <div><div class="name" style="font-size:34px">HollowBirch</div><div class="sub" style="font-size:19px">Therapy Dogs</div></div>
</div>
<p class="abs" style="left:515px;top:4643px;width:330px;font-size:13.5px;color:var(--purple)">Stay up to date with therapy visits, community events, volunteer opportunities, and heartwarming stories.</p>
<div class="social" style="left:893px" aria-label="Social link"></div>
<div class="social" style="left:943px" aria-label="Social link"></div>
<div class="social" style="left:993px" aria-label="Social link"></div>
<div class="social" style="left:1043px" aria-label="Social link"></div>
<div class="abs" style="left:515px;top:4720px;width:572px;height:1px;background:var(--purple)"></div>
<div class="abs flinks"><span>About</span><span>Our Team</span><span>Request a Visit</span><span>Donors &amp; Referrals</span><span>Contact</span></div>
<div class="btn btn-yellow" style="left:515px;top:4838px;width:254px">Request a Therapy Visit</div>
<div class="btn btn-purple" style="left:790px;top:4838px;width:184px">Join Our Team</div>
<p class="abs" style="left:515px;top:4908px;font-size:13px;color:var(--purple)">2026 HollowBirch Therapy Dogs. All Rights Reserved.</p>

</body>
</html>
```